Harbel Shipping

A flyer that sells both air and sea freight services. We had an attempt at this and wanted a fresh concept from your designers. Colors should be vibrant and the text readable on a digital billboard as well. Our attempt is attached along with our logo file.

Designers***The contents on our attempt flyer should be applied to your flyer design.

Thanks!

Industry/Entity Type

Shipping

```html
<!DOCTYPE html>
<html lang="en">
<head>
<meta charset="utf-8">
<title>Harbel Shipping – Flyer</title>
<link href="https://fonts.googleapis.com/css2?family=Red+Hat+Display:ital,wght@0,700;0,900;1,700;1,900&display=swap" rel="stylesheet">
<style>
  :root {
    --stage: #b9b9b9;
    --red: #a3161f;
    --navy: #1b2c4c;
    --sky-top: #ffffff;
    --sky-1: #c6def3;
    --sky-2: #8fcbec;
    --sky-3: #a9dde4;
    --sky-4: #cfe9d6;
    --sea-top: #3f84c6;
    --sea-bottom: #22a5b3;
    --plane-light: #f4f6f8;
    --plane-shade: #cfd6dd;
    --ship-light: #d2383c;
    --ship-dark: #8e1c22;
  }
  html, body { margin: 0; padding: 0; }
  body {
    width: 1200px; height: 1200px; overflow: hidden;
    background: var(--stage);
    font-family: "Red Hat Display", sans-serif;
    position: relative;
  }
  .flyer {
    position: absolute; left: 190px; top: 70px;
    width: 819px; height: 1059px; overflow: hidden;
    background: linear-gradient(180deg, var(--sky-top) 0%, var(--sky-1) 18%, var(--sky-2) 48%, var(--sky-3) 72%, var(--sky-4) 88%);
    box-shadow: 0 6px 18px rgba(0,0,0,.35);
  }
  .flyer > * { position: absolute; margin: 0; line-height: 1; }
  .brand { left: 52px; top: 40px; width: 170px; text-align: center; }
  .brand__dot { display: block; width: 100px; height: 100px; margin: 0 auto 14px; border-radius: 50%; background: var(--red); }
  .brand__name { color: var(--red); font-weight: 900; font-size: 25px; letter-spacing: .5px; line-height: 1.05; }
  .headline { right: 63px; text-align: right; font-weight: 900; letter-spacing: -2px; }
  .headline--save { top: 40px; color: var(--red); font-size: 76px; }
  .headline--ship { top: 120px; color: var(--navy); font-style: italic; font-size: 76px; letter-spacing: -2.5px; }
  .rule { left: 63px; width: 694px; height: 1px; background: var(--navy); }
  .offer-title { left: 63px; top: 296px; color: var(--red); font-weight: 900; font-size: 62px; letter-spacing: -1.5px; }
  .services { left: 63px; top: 364px; padding: 0; list-style: none; color: var(--navy); font-weight: 900; font-style: italic; font-size: 40px; letter-spacing: -.5px; }
  .services li { height: 44px; }
  .plane { left: 482px; top: 354px; width: 284px; height: 60px; border-radius: 30px;
    background: linear-gradient(170deg, var(--plane-light), var(--plane-shade)); }
  .signup { left: 63px; width: 694px; top: 640px; text-align: center; color: var(--navy); font-weight: 900; font-style: italic; font-size: 31px; letter-spacing: 1.2px; }
  .site { left: 63px; width: 694px; top: 682px; text-align: center; color: var(--red); font-weight: 900; font-size: 33px; letter-spacing: .8px; }
  .contact { left: 63px; top: 771px; display: flex; gap: 32px; color: var(--navy); font-weight: 900; font-style: italic; font-size: 23px; letter-spacing: .6px; }
  .contact span { display: inline-flex; align-items: center; gap: 8px; }
  .social { top: 830px; width: 38px; height: 37px; border-radius: 7px; background: var(--navy); }
  .social--a { left: 63px; }
  .social--b { left: 134px; }
  .sea { left: 0; top: 914px; width: 819px; height: 145px; background: linear-gradient(180deg, var(--sea-top), var(--sea-bottom)); }
  .ship { left: 244px; top: 816px; width: 575px; height: 154px; border-radius: 14px 0 0 40px;
    background: linear-gradient(180deg, var(--ship-light) 0%, var(--ship-dark) 100%); }
</style>
</head>
<body>
  <main class="flyer">
    <div class="brand">
      <span class="brand__dot"></span>
      <div class="brand__name">HARBEL<br>SHIPPING</div>
    </div>

    <h1 class="headline headline--save">SAVE MONEY</h1>
    <h2 class="headline headline--ship">SHIP BETTER</h2>

    <div class="rule" style="top:236px"></div>

    <h3 class="offer-title">WE OFFER</h3>
    <ul class="services">
      <li>CARGO</li>
      <li>CONSOLIDATION</li>
      <li>AIR FREIGHT</li>
      <li>CUSTOM CLEARANCE</li>
      <li>LOCAL PARCELHUB BOX</li>
    </ul>

    <div class="plane" role="img" aria-label="Photo of a passenger jet in flight"></div>

    <div class="rule" style="top:624px"></div>
    <p class="signup">SIGN UP TO RECIEVE YOUR SUITE #</p>
    <p class="site">WWW.HARBELFREIGHTBAHAMAS.COM</p>
    <div class="rule" style="top:722px"></div>

    <div class="contact">
      <span>
        <svg width="22" height="22" viewBox="0 0 24 24" aria-hidden="true"><path fill="var(--navy)" d="M6.6 10.8a15.1 15.1 0 0 0 6.6 6.6l2.2-2.2a1 1 0 0 1 1-.25 11.4 11.4 0 0 0 3.6.57 1 1 0 0 1 1 1V20a1 1 0 0 1-1 1A17 17 0 0 1 3 4a1 1 0 0 1 1-1h3.5a1 1 0 0 1 1 1c0 1.25.2 2.45.57 3.57a1 1 0 0 1-.25 1z"/></svg>
        555-0142
      </span>
      <span>
        <svg width="22" height="22" viewBox="0 0 24 24" aria-hidden="true"><path fill="var(--navy)" d="M12 3 2 12h3v9h5v-6h4v6h5v-9h3z"/></svg>
        #24 PALMETTO RD. NASSAU, BAHAMAS
      </span>
    </div>

    <span class="social social--a" aria-label="Social profile"></span>
    <span class="social social--b" aria-label="Social profile"></span>

    <div class="sea"></div>
    <div class="ship" role="img" aria-label="Photo of a container ship loaded with cargo at sea"></div>
  </main>
</body>
</html>
```